Residential building / Apartments for sale landing page

I need a website / landing page design for my latest development project - a residential building with 70+ apartments for sale. I need the design in layers in Photoshop/Illustrator/InDesign format with all the icons/shapes/maps/graphic assets in vector format (svg, ai, eps) as much as possible.

I prefer white website and please consider the performance/coding experience. We're not making something suitable only for a design contest with fancy parallax effects and confusing animations. We're trying to create usable and clean UI with good UX.

The website will be custom coded, i.e. I'm not using WordPress.

I know that the existing 3D photos are not good but for now you can use them or replace them with some stock photos. I'm going to create new 3D photos soon.

Industry/Entity Type

Real Estate Development

Number of Pages Required

1 page

```html
<!DOCTYPE html>
<html lang="en">
<head>
<meta charset="utf-8">
<title>Cloud Grove – Apartments for Sale</title>
<link href="https://fonts.googleapis.com/css2?family=Montserrat:wght@400;500;600;700&display=swap" rel="stylesheet">
<style>
:root{
  --blue:#4163e6;
  --green:#8cc63f;
  --ink:#222;
  --muted:#555;
  --line:#d9dff0;
  --dark:#2a2a2a;
  --red:#e53935;
}
*{box-sizing:border-box;margin:0;padding:0}
html,body{width:1200px;height:4922px;overflow:hidden;background:#fff}
body{font-family:'Montserrat',sans-serif;color:var(--ink)}
.page{position:relative;width:1200px;height:4922px;overflow:hidden}
.abs{position:absolute}
/* top */
.topbar{left:0;top:0;width:1200px;height:34px;background:#f5f7fb;font-size:10px}
.topbar span{position:absolute;right:110px;top:12px}
.topbar b{color:var(--red);font-weight:500}
.nav{left:0;top:34px;width:1200px;height:61px;background:#fff;border-bottom:1px solid #eee}
.brand{position:absolute;left:113px;top:22px;font-size:17px;font-weight:700;letter-spacing:.5px;color:var(--ink)}
.menu{position:absolute;left:254px;top:22px;display:flex;gap:20px;font-size:12px}
.menu a{color:var(--ink);text-decoration:none}
.menu a.on{color:var(--green)}
.nav-phone{position:absolute;left:862px;top:24px;font-size:11px}
.btn-blue{position:absolute;background:var(--blue);color:#fff;font-size:12px;display:flex;align-items:center;justify-content:center}
/* hero */
.hero{left:0;top:95px;width:1200px;height:660px;background:linear-gradient(180deg,#f3f5f6 0%,#e7ecee 18%,#9aa79b 35%,#6f8f63 55%,#8aa07c 72%,#c7cec8 100%)}
.hero-title{left:0;top:160px;width:1200px;text-align:center;font-size:46px;font-weight:600}
.hero-band{left:264px;top:231px;width:670px;height:40px;background:var(--green);color:#fff;font-size:26px;display:flex;align-items:center;justify-content:center}
.hero-price{left:0;top:282px;width:1200px;text-align:center;font-size:22px}
.hero-btn{left:522px;top:336px;width:156px;height:46px;border:2px solid #222;font-size:18px;display:flex;align-items:center;justify-content:center}
/* headings */
.h2{left:0;width:1200px;text-align:center;font-size:31px;font-weight:400}
.lead{left:150px;width:900px;text-align:center;font-size:12px;line-height:22px;color:var(--muted)}
/* welcome */
.welcome-title{left:111px;top:848px;font-size:31px}
.welcome-title em{font-style:normal;color:var(--green)}
.welcome-text{left:111px;top:908px;width:460px;font-size:11px;line-height:23px;color:var(--muted)}
/* apartments */
.tab{position:absolute;top:1382px;height:32px;color:#fff;font-size:13px;display:flex;align-items:center;justify-content:center}
.select-label{left:946px;top:1390px;font-size:13px;font-weight:600}
.select{left:1005px;top:1384px;width:83px;height:28px;border:1px solid #bbb;font-size:11px;padding:6px 8px}
.unit-photo{left:111px;top:1468px;width:159px;height:156px;background:linear-gradient(160deg,#eef0ef,#b9ab9b 60%,#6a5b50)}
.spec{left:279px;top:1468px;width:808px;height:156px;border:1px solid var(--line);background:#f7f9ff}
.cell{position:absolute;height:78px;border-right:1px solid var(--line);text-align:center;font-size:11px;padding-top:16px}
.cell small{display:block;margin-top:12px;font-size:10px;color:#999}
.cell .link{color:var(--red);text-decoration:underline;font-size:8px}
.pop{position:absolute;background:#fff;border:1px solid var(--line);font-size:9px;color:#666}
.price{left:892px;top:1652px;font-size:19px}
.price span{color:var(--green);margin-right:14px}
/* benefits */
.forest{left:0;top:1842px;width:1200px;height:531px;background:radial-gradient(circle at 20% 30%,#6ea83b,transparent 40%),radial-gradient(circle at 80% 70%,#4f8a2a,transparent 45%),linear-gradient(135deg,#3f7a24,#7cb545 50%,#3b6d22)}
.blue-box{background:var(--blue);color:#fff;font-size:12px;line-height:23px}
.panel{left:111px;top:1945px;width:976px;height:428px;background:#fff}
.plan{left:111px;top:1975px;width:489px;height:398px;background:linear-gradient(135deg,#f3f3ef,#e4e4dc 60%,#dfe0c7)}
.features{left:672px;top:2008px;list-style:none}
.features li{display:flex;align-items:center;height:32px;font-size:11px}
.features svg{width:20px;height:20px;margin-right:16px;stroke:var(--green);fill:none;stroke-width:1.6}
.dash{left:600px;top:2379px;height:86px;border-left:1px dashed var(--green)}
/* construction */
.spec-list{left:633px;top:2686px;width:450px;list-style:none}
.spec-list li{font-size:11px;line-height:19px;color:#444;margin-bottom:12px}
.spec-list b{color:var(--green);font-weight:700}
/* location */
.map{left:0;top:3283px;width:1200px;height:453px;background:linear-gradient(160deg,#eef1f6,#e3e8f0 50%,#edf0f5)}
/* gallery */
.shot{position:absolute;top:3906px;width:234px;height:218px}
.shot-date{position:absolute;top:4143px;font-size:12px}
.view{position:absolute;top:4135px;width:90px;height:27px;background:var(--green);color:#fff;font-size:12px;display:flex;align-items:center;justify-content:center;gap:8px}
/* contact */
.grass{left:0;top:4262px;width:1200px;height:305px;background:linear-gradient(180deg,#fff 0%,#eef3e4 45%,#8fb36a 80%,#5c7f3a 100%)}
.dark{left:0;top:4567px;width:1200px;height:355px;background:var(--dark)}
.card{left:157px;top:4322px;width:506px;height:484px;background:#fff}
.card-blue{left:663px;top:4322px;width:380px;height:484px;background:var(--blue);color:#fff}
.field{position:absolute;border:1px solid #999;font-size:11px;padding:0 12px;display:flex;align-items:center;color:#444}
.info{position:absolute;left:40px;display:flex;align-items:center;gap:24px;font-size:11px}
.ring{width:40px;height:40px;border:1px solid rgba(255,255,255,.7);border-radius:50%;display:flex;align-items:center;justify-content:center}
.ring svg{width:16px;height:16px;fill:#fff}
.foot-links{left:158px;top:4832px;display:flex;gap:16px;font-size:10px;color:#fff}
.copy{left:0;top:4888px;width:1200px;text-align:center;font-size:9px;color:#ccc}
</style>
</head>
<body>
<div class="page">

<div class="abs topbar"><span>Language: BG <b>EN</b></span></div>
<header class="abs nav">
  <div class="brand">CLOUD GROVE</div>
  <nav class="menu"><a class="on">Cloud Grove</a><a>The project</a><a>Apartments/Sales</a><a>Location</a><a>Gallery</a></nav>
  <div class="nav-phone">+ 00 12 3456 7890</div>
  <div class="btn-blue" style="left:975px;top:17px;width:114px;height:27px">Contact us</div>
</header>

<section class="abs hero" role="img" aria-label="Rendering of a green terraced residential building with mountains behind"></section>
<svg class="abs" style="left:0;top:660px" width="1200" height="100" viewBox="0 0 1200 100">
  <path d="M0 95 C300 30 700 10 1200 75 L1200 100 L0 100Z" fill="#fff"/>
  <path d="M0 92 C300 28 700 8 1200 72 L1200 90 C700 30 300 50 0 100Z" fill="#8cc63f"/>
</svg>
<h1 class="abs hero-title">Sale of Apartments</h1>
<div class="abs hero-band">Directly from the investor with 10% discount</div>
<div class="abs hero-price">Price from 200 EUR/m2</div>
<div class="abs hero-btn">Buy now</div>

<h2 class="abs welcome-title">Welcome to <em>Cloud Grove</em></h2>
<p class="abs welcome-text">Lorem ipsum dolor sit amet, consectetur adipiscing elit. Sed bibendum elit orci, vitae ultricies neque finibus quis. Maecenas a felis eu ipsum molestie volutpat ut nec nisl. Curabitur ut leo ac elit ultrices iaculis eget eget justo. Sed placerat nulla ac egestas finibus. Etiam hendrerit quis tellus nec maximus. Duis eget lacus ut nulla fermentum vehicula eu a tortor. Nam viverra pretium augue, vel dapibus magna porttitor eget. Sed luctus orci eget finibus pharetra. In vitae nisl justo.</p>
<svg class="abs" style="left:631px;top:780px" width="460" height="410" viewBox="0 0 460 410" role="img" aria-label="Photo of a couple looking out from a bright apartment terrace">
  <defs><linearGradient id="wg" x1="0" y1="0" x2="1" y2="1"><stop offset="0" stop-color="#dfe7ee"/><stop offset=".6" stop-color="#b9c3c8"/><stop offset="1" stop-color="#6f6a62"/></linearGradient></defs>
  <path d="M40 60 C120 0 330 -10 420 90 C480 170 440 300 340 370 C250 430 90 400 40 300 C0 220 -20 110 40 60Z" fill="url(#wg)" stroke="#8cc63f" stroke-width="6"/>
</svg>

<h2 class="abs h2" style="top:1257px">Apartments</h2>
<p class="abs lead" style="top:1307px">Lorem ipsum dolor sit amet, consectetur adipiscing elit. Sed bibendum elit orci, vitae ultricies neque finibus quis. Lorem ipsum dolor sit amet.</p>
<div class="tab" style="left:111px;width:116px;background:var(--blue)">Type 1</div>
<div class="tab" style="left:233px;width:115px;background:var(--green)">Type 2</div>
<div class="tab" style="left:355px;width:117px;background:var(--green)">Type 3</div>
<div class="abs select-label">Select:</div>
<div class="abs select">Floor 1 <span style="float:right">⌄</span></div>
<div class="abs unit-photo" role="img" aria-label="Photo of an apartment living room"></div>
<div class="abs spec">
  <div class="cell" style="left:0;top:0;width:139px">Unit<small>12</small></div>
  <div class="cell" style="left:139px;top:0;width:140px">Entrance/Block<small>1</small></div>
  <div class="cell" style="left:279px;top:0;width:139px">Beds<small><span style="color:var(--red)">2</span> <span class="link">See Dimensions</span></small></div>
  <div class="cell" style="left:418px;top:0;width:140px">Bathrooms<small>1</small></div>
  <div class="cell" style="left:558px;top:0;width:250px;border-right:0">Area ⌄</div>
  <div style="position:absolute;left:0;top:78px;width:808px;border-top:1px solid var(--line)"></div>
  <div class="cell" style="left:0;top:78px;width:139px">Status ⌄</div>
  <div class="cell" style="left:139px;top:78px;width:140px">View<small>yes</small></div>
  <div class="cell" style="left:279px;top:78px;width:139px">Parking space<small>yes</small></div>
  <div class="cell" style="left:418px;top:78px;width:140px">MM tax<small>12%</small></div>
  <div class="cell" style="left:558px;top:78px;width:250px;border-right:0">Unit plan + Floor plan<small><span class="link">view more</span></small></div>
  <div class="pop" style="left:616px;top:38px;width:217px;height:44px;display:grid;grid-template-columns:1fr 1fr 1.3fr;padding:6px 10px;row-gap:10px"><span>Apartment</span><span>Terraces</span><span>Common area</span><span style="color:#aaa">1200 sqft</span><span style="color:#aaa">200 sqft</span><span style="color:#aaa">1000 sqft</span></div>
  <div class="pop" style="left:55px;top:115px;width:114px;height:42px;display:grid;grid-template-columns:1fr 1fr;padding:5px 8px;row-gap:10px"><span>Available</span><span>Sold</span><span style="color:#aaa">9</span><span style="color:#aaa">3</span></div>
</div>
<div class="abs price"><span>Price:</span>200 EUR/m2</div>

<h2 class="abs" style="left:108px;top:1727px;font-size:31px;font-weight:400">Benefits</h2>
<div class="abs forest" role="img" aria-label="Aerial photo of dense green tree canopy"></div>
<div class="abs panel"></div>
<div class="abs blue-box" style="left:111px;top:1794px;width:489px;height:151px;padding:24px 26px">Lorem ipsum dolor sit amet, consectetur adipiscing elit. Sed bibendum elit orci, vitae ultricies neque finibus quis. Lorem ipsum dolor sit amet, consectetur adipiscing elit. Sed bibendum elit orci, vitae ultricies neque finibus quis.</div>
<div class="abs plan" role="img" aria-label="Site plan drawing of the courtyard and building blocks"></div>
<ul class="abs features">
  <li><svg viewBox="0 0 20 20"><path d="M10 2 L5 10 H8 L4 17 H16 L12 10 H15Z"/></svg>Green areas and gardens</li>
  <li><svg viewBox="0 0 20 20"><rect x="3" y="3" width="14" height="14"/><path d="M8 14V6h3a2.5 2.5 0 010 5H8"/></svg>Parking spaces</li>
  <li><svg viewBox="0 0 20 20"><circle cx="5" cy="13" r="3.5"/><circle cx="15" cy="13" r="3.5"/><path d="M5 13 L9 6 L15 13 M8 6h3"/></svg>Bicycle parking</li>
  <li><svg viewBox="0 0 20 20"><circle cx="12" cy="3.5" r="1.5"/><path d="M11 6 L8 11 L11 13 L10 18 M8 11 L4 12 M11 8 L15 10"/></svg>Outside workout area</li>
  <li><svg viewBox="0 0 20 20"><rect x="5" y="2" width="10" height="16" rx="1"/><path d="M8 7h4M8 11h4"/></svg>NFC controlled access</li>
  <li><svg viewBox="0 0 20 20"><circle cx="10" cy="3.5" r="1.5"/><path d="M10 6v6 M4 8h12 M10 12 L7 18 M10 12 L13 18"/></svg>Outdoor Yoga area</li>
  <li><svg viewBox="0 0 20 20"><path d="M2 10 A8 6 0 0118 10Z M10 10v8"/></svg>Relaxation area</li>
  <li><svg viewBox="0 0 20 20"><path d="M2 17h16 M4 17 L10 6 L16 17 M7 12h6"/></svg>Childrens play ground</li>
  <li><svg viewBox="0 0 20 20"><path d="M2 14c2-2 4-2 6 0s4 2 6 0 3-1 4 0 M6 10 L9 6h3"/><circle cx="14" cy="7" r="1.5"/></svg>Pool</li>
  <li><svg viewBox="0 0 20 20"><path d="M6 2v16 M3 2v5a3 3 0 006 0V2 M14 18V2c3 2 3 7 0 8"/></svg>Restaurant</li>
</ul>
<div class="abs dash"></div>

<h2 class="abs h2" style="top:2485px">Construction features</h2>
<p class="abs lead" style="top:2536px">Lorem ipsum dolor sit amet, consectetur adipiscing elit. Sed bibendum elit orci, vitae ultricies neque finibus quis. Lorem ipsum dolor sit amet, consectetur adipiscing elit. Sed bibendum elit orci, vitae ultricies neque finibus quis.</p>
<svg class="abs" style="left:112px;top:2643px" width="462" height="418" viewBox="0 0 462 418" role="img" aria-label="Photo of a bright living room with city view windows">
  <defs><linearGradient id="cg" x1="0" y1="0" x2="1" y2="1"><stop offset="0" stop-color="#f1f3f4"/><stop offset=".55" stop-color="#c9d6df"/><stop offset="1" stop-color="#9aa3a8"/></linearGradient></defs>
  <path d="M60 60 C150 -10 360 -5 430 60 C480 120 460 260 380 340 C300 410 140 425 60 350 C-10 280 0 110 60 60Z" fill="url(#cg)" stroke="#8cc63f" stroke-width="6"/>
</svg>
<ul class="abs spec-list">
  <li><b>Glazewell Windows</b> - 5 chamber noise reducing glazing with high temperature and noise insulation efficiency</li>
  <li><b>Brickmoor bricks</b> - Austrian Brickmoor ThermoCore bricks with porous system and 25 cm thick outer walls</li>
  <li><b>High Ceilings</b> - 2.70m high ceilings giving the light and space you need</li>
  <li><b>Thermal Insulation System Thermaline</b> - Thermaline Silicone Plaster Thermal Insulation System 10 cm thick and 15 cm thick from the north walls</li>
  <li><b>Air conditioners</b> - All air conditioners piping systems are installed - ready to plug in the inside and outside body of the aircon system</li>
  <li><b>HPL ventilated facade Facadex GmbH</b> - Suspended ventilated facade with highly pressed laminated panels by Facadex GmbH in wood color</li>
  <li><b>Panoramic Vistaline over looking the park</b> - Giving you the everyday glimpse over the inside garden and putting a smile on your face</li>
  <li><b>Water proofing with PVC membrane Sealora</b> - PVC membrane with high puncture and tear resistance, UV resistance and vapor permeability</li>
</ul>

<h2 class="abs h2" style="top:3175px">Location</h2>
<p class="abs lead" style="top:3228px">Lorem ipsum dolor sit amet, consectetur adipiscing elit. Sed bibendum elit orci, vitae ultricies neque finibus quis. Lorem ipsum dolor sit amet.</p>
<div class="abs map" role="img" aria-label="Street map showing the building location and nearby landmarks"></div>

<h2 class="abs h2" style="top:3821px">Gallery</h2>
<div class="abs blue-box" style="left:111px;top:3906px;width:235px;height:258px;padding:30px 24px">Lorem ipsum dolor sit amet, consectetur adipiscing elit. Sed bibendum elit orci, vitae ultricies neque finibus quis. Lorem ipsum dolor sit amet, consectetur adipiscing elit. Sed bibendum elit orci, vitae ultricies neque finibus quis.</div>
<div class="shot" style="left:359px;background:linear-gradient(160deg,#f4f4f2,#cfcac2 60%,#6d655d)" role="img" aria-label="Photo of a dining room with chandelier"></div>
<div class="shot" style="left:606px;background:linear-gradient(160deg,#eef2f4,#d7d3cb 60%,#8d7f70)" role="img" aria-label="Photo of a bright bedroom interior"></div>
<div class="shot" style="left:852px;background:linear-gradient(160deg,#f5f5f5,#dcdcd8 60%,#8b8884)" role="img" aria-label="Photo of a high-ceiling living room"></div>
<div class="shot-date" style="left:363px">April 2021</div>
<div class="view" style="left:502px">View <span>⊙</span></div>
<div class="shot-date" style="left:608px">March 2021</div>
<div class="view" style="left:751px">View <span>⊙</span></div>
<div class="shot-date" style="left:855px">February 2021</div>
<div class="view" style="left:997px">View <span>⊙</span></div>

<div class="abs grass" role="img" aria-label="Close-up photo of green grass"></div>
<div class="abs dark"></div>
<div class="abs card">
  <h2 style="position:absolute;left:34px;top:44px;font-size:31px;font-weight:400">Contact us</h2>
  <div class="field" style="left:34px;top:115px;width:445px;height:42px">Name *</div>
  <div class="field" style="left:34px;top:176px;width:222px;height:42px">Email *</div>
  <div class="field" style="left:269px;top:176px;width:210px;height:42px">Phone *</div>
  <div class="field" style="left:34px;top:239px;width:445px;height:79px;align-items:flex-start;padding-top:12px">Message</div>
  <div style="position:absolute;left:34px;top:335px;font-size:10px;display:flex;align-items:center;gap:10px;color:#444"><span style="width:13px;height:13px;border:1px solid #999;display:inline-block"></span>I agree with the privacy policy of Cloud Grove</div>
  <div style="position:absolute;left:34px;top:367px;width:155px;height:42px;background:var(--green);color:#fff;font-size:13px;display:flex;align-items:center;justify-content:center">SUBMIT</div>
  <div style="position:absolute;left:34px;top:426px;font-size:8px;color:var(--red)">* Fields are important</div>
</div>
<div class="abs card-blue">
  <div style="position:absolute;left:0;top:132px;width:380px;text-align:center;font-size:28px;font-weight:700">CLOUD GROVE</div>
  <div class="info" style="top:237px"><div class="ring"><svg viewBox="0 0 16 16"><path d="M8 1a5 5 0 00-5 5c0 4 5 9 5 9s5-5 5-9a5 5 0 00-5-5zm0 7a2 2 0 110-4 2 2 0 010 4z"/></svg></div><span style="width:220px;line-height:18px">Lorem ipsum dolor sit amet, consectetur adipiscing elit</span></div>
  <div class="info" style="top:309px"><div class="ring"><svg viewBox="0 0 16 16"><path d="M4 1l2.5 3-1.5 2c1 2 3 4 5 5l2-1.5 3 2.5-1.5 2.5C7 14 2 9 1.5 3.5Z"/></svg></div><span style="font-size:19px;font-weight:700">+ 00 12 3456 7890</span></div>
  <div class="info" style="top:380px"><div class="ring"><svg viewBox="0 0 16 16"><path d="M1 3h14v10H1z M1 3l7 6 7-6" fill="none" stroke="#fff" stroke-width="1.4"/></svg></div><span>info@cloudgrove.example</span></div>
</div>
<div class="abs foot-links"><span>Cloud Grove</span><span>The project</span><span>Apartments/Sales</span><span>Location</span><span>Gallery</span></div>
<div class="abs" style="left:997px;top:4830px;width:16px;height:16px;border:1px solid #fff;border-radius:50%"></div>
<div class="abs" style="left:1024px;top:4830px;width:16px;height:16px;border:1px solid #fff;border-radius:50%"></div>
<div class="abs copy">Copyright © 2021 cloudgrove.example All Right Reserved.</div>

</div>
</body>
</html>
```